Adelaide based cleaning and remediation business needs a website design

We are launching a new company with no clients as yet so we don't have the benefit of Trelvox Ratings to build confidence. We can use our  past work history with other employers in the industry to give some credibility. Happy to use any colour scheme as long as it look interesting when people click on the site it gets there attention. enquiry . I have supplied a mock up the important information and various photos as they tell a lot of the story.

```html
<!DOCTYPE html>
<html lang="en">
<head>
<meta charset="utf-8">
<title>Certiva – Cleaning &amp; Remediation Adelaide</title>
<link href="https://fonts.googleapis.com/css2?family=Poppins:wght@400;500;600;700;800&display=swap" rel="stylesheet">
<style>
:root{
  --green:#1e3b2f;
  --green-2:#2b4a3c;
  --yellow:#f5c842;
  --ink:#1b1b1b;
  --muted:#6d6d6d;
  --bg:#ffffff;
  --soft:#f6f5ef;
  --line:#e6e4dc;
}
*{box-sizing:border-box;margin:0;padding:0}
html,body{width:1200px;height:4828px;overflow:hidden}
body{font-family:"Poppins",sans-serif;color:var(--ink);background:var(--bg);font-size:13px;line-height:1.6}
.btn{display:inline-flex;align-items:center;gap:8px;background:var(--yellow);color:var(--ink);font-weight:600;font-size:12px;border-radius:30px;padding:10px 22px;text-decoration:none}
.eyebrow{font-size:12px;font-weight:600;color:var(--muted);margin-bottom:6px}
.title{font-size:34px;font-weight:700;line-height:1.2}
.lead{color:var(--muted);font-size:13px}
.ph{display:block}

/* header */
.site-header{height:68px;display:flex;align-items:center;justify-content:space-between;padding:0 40px 0 60px;background:#fff;position:relative;z-index:2}
.brand{display:flex;align-items:center;gap:10px;font-weight:800;font-size:26px;color:var(--green)}
.brand-dot{width:30px;height:30px;border-radius:50%;background:var(--green)}
.nav{display:flex;gap:26px;font-size:12px;font-weight:500;margin-left:auto;margin-right:30px}
.nav a{color:var(--ink);text-decoration:none}
.header-cta{display:flex;align-items:center;gap:18px}
.phone{display:flex;align-items:center;gap:8px;font-weight:700;font-size:17px}

/* hero */
.hero{height:692px;position:relative;overflow:hidden}
.hero-photo{position:absolute;inset:0;background:linear-gradient(120deg,#2a2621 0%,#4a4036 40%,#3a342d 70%,#1f1c19 100%)}
.hero-shade{position:absolute;inset:0;background:linear-gradient(90deg,rgba(0,0,0,.55),rgba(0,0,0,.15))}
.hero-copy{position:absolute;left:172px;top:196px;color:#fff}
.hero-copy h1{font-size:40px;font-weight:800;line-height:1.1;text-transform:uppercase}
.hero-copy p{font-size:15px;margin:12px 0 26px;font-weight:500}
.hero-wave{position:absolute;left:0;bottom:0;width:1200px;height:130px}

/* about */
.about{height:400px;display:flex;padding:0 0 0 250px;gap:40px;position:relative}
.about-media{position:relative;width:380px;height:330px}
.about-media .a1{position:absolute;left:0;top:0;width:220px;height:185px;border-radius:8px;background:linear-gradient(135deg,#3d3a35,#6b5f4f)}
.about-media .a2{position:absolute;left:234px;top:0;width:140px;height:120px;border-radius:8px;background:linear-gradient(135deg,#7e8a93,#c9ced2)}
.about-media .a3{position:absolute;left:130px;top:130px;width:244px;height:200px;border-radius:8px;background:linear-gradient(135deg,#4c4a45,#8c867a)}
.years{position:absolute;left:0;top:200px;width:120px;height:120px;background:var(--soft);border-radius:8px;padding:18px;text-align:left}
.years-icon{width:26px;height:26px;border-radius:50%;background:var(--green)}
.years b{display:block;font-size:28px;margin-top:4px}
.years span{font-size:10px;color:var(--muted)}
.about-copy{width:330px;padding-top:6px}
.checks{display:grid;grid-template-columns:1fr 1fr;gap:8px;margin:16px 0 20px;font-size:11px;font-weight:600}
.checks li{list-style:none;display:flex;align-items:center;gap:6px}
.checks i{width:8px;height:8px;border-radius:50%;background:var(--green)}
.about-deco{position:absolute;right:0;top:120px;width:150px;height:240px}

/* services */
.services{height:440px;position:relative;background:var(--soft)}
.services-photo{position:absolute;left:0;top:0;width:250px;height:400px;background:linear-gradient(160deg,#365b78,#6c8a9c 60%,#b2a35a)}
.services-intro{position:absolute;left:258px;top:60px;width:222px;height:250px;background:var(--yellow);border-radius:10px;padding:24px}
.services-intro h2{font-size:24px;font-weight:700;line-height:1.2;margin-bottom:10px}
.services-intro .btn{background:var(--green);color:#fff;margin-top:14px}
.service-cards{position:absolute;left:498px;top:60px;display:flex;gap:18px}
.card{width:212px;height:250px;background:#fff;border-radius:10px;padding:22px}
.card-icon{width:46px;height:46px;border-radius:8px;background:var(--soft);display:flex;align-items:center;justify-content:center;margin-bottom:14px}
.card h3{font-size:16px;font-weight:700;line-height:1.25;margin-bottom:8px}
.card p{font-size:11px;color:var(--muted);margin-bottom:14px}
.card .btn{padding:7px 16px;font-size:11px}
.dots{display:flex;gap:6px;justify-content:center}
.dots i{width:7px;height:7px;border-radius:50%;background:#c9c7bd}
.dots i.on{background:var(--ink);width:18px;border-radius:4px}
.services .dots{position:absolute;left:490px;top:350px}

/* why */
.why{height:720px;background:var(--green);color:#fff;padding:70px 250px 0 250px;position:relative}
.why-top{display:flex;justify-content:space-between}
.why-top .eyebrow{color:#cfd8d2}
.why-top .title{width:360px;font-size:30px}
.why-top .lead{width:300px;color:#cfd8d2;font-size:12px;border-left:2px solid var(--yellow);padding-left:14px;height:fit-content}
.stats{display:flex;justify-content:space-between;margin:40px 0 36px}
.stat b{display:block;font-size:28px;font-weight:700}
.stat span{font-size:11px;color:#cfd8d2}
.why-video{width:700px;height:300px;border-radius:10px;position:relative;background:linear-gradient(180deg,#5e5e5a,#c8c3b9 70%,#a89680)}
.play{position:absolute;left:50%;top:50%;transform:translate(-50%,-50%);width:56px;height:56px;border-radius:50%;background:var(--yellow);display:flex;align-items:center;justify-content:center}

/* projects */
.projects{height:670px;text-align:center;padding-top:110px}
.projects .lead{width:520px;margin:12px auto 34px}
.project-grid{display:flex;gap:12px;justify-content:center;margin-bottom:26px}
.project-grid .ph{width:222px;height:280px;border-radius:8px}

/* cta */
.cta{height:310px;position:relative;overflow:hidden}
.cta-bg{position:absolute;inset:0;background:linear-gradient(90deg,#213a2d 0%,#2a4633 45%,#6b7560 60%,#c9b9a3 100%)}
.cta-woman{position:absolute;right:0;top:0;width:560px;height:310px;background:linear-gradient(120deg,#8c7f6c,#d6c7b1 50%,#7a5e68)}
.cta-copy{position:absolute;left:250px;top:92px;color:#fff}
.cta-copy .eyebrow{color:#d7e0da}
.cta-copy h2{font-size:30px;font-weight:700;line-height:1.2;width:340px;margin-bottom:18px}

/* testimonials */
.testimonials{height:600px;text-align:center;padding-top:120px;position:relative}
.stars{display:flex;gap:4px;justify-content:center;margin:30px 0 14px}
.quote{width:560px;margin:0 auto;color:var(--muted);font-size:12px}
.reviewer{margin-top:24px}
.avatars{display:flex;justify-content:center;gap:6px;margin-bottom:10px}
.avatars i{width:30px;height:30px;border-radius:50%;background:linear-gradient(135deg,#b89a82,#6d5546)}
.avatars i.on{width:36px;height:36px}
.reviewer b{display:block;font-size:14px}
.reviewer span{font-size:11px;color:var(--muted)}
.arrow{position:absolute;top:308px;width:36px;height:36px;border-radius:50%;background:var(--green);display:flex;align-items:center;justify-content:center}
.arrow.prev{left:250px}.arrow.next{right:250px}

/* blog */
.blog{height:690px;text-align:center;padding-top:60px}
.blog .lead{width:520px;margin:12px auto 36px}
.posts{display:flex;justify-content:center;gap:18px}
.post{width:222px;text-align:left}
.post .ph{height:200px;border-radius:8px;margin-bottom:14px}
.post h3{font-size:14px;font-weight:700;text-align:center;line-height:1.3;margin-bottom:10px}
.post .btn{display:flex;width:fit-content;margin:0 auto;padding:7px 16px;font-size:11px}
.payments{display:flex;gap:8px;justify-content:flex-end;padding-right:250px;margin-top:64px}
.payments i{width:28px;height:18px;border-radius:3px;background:#d7d7d2}

/* footer */
.site-footer{height:238px;background:var(--green);color:#fff;position:relative;padding:14px 40px 0 250px}
.footer-grid{display:flex;gap:26px}
.footer-brand{width:150px}
.footer-logo{width:130px;height:64px;background:#fff;border-radius:6px;display:flex;align-items:center;justify-content:center;gap:6px;font-weight:800;font-size:20px;color:var(--green);margin-bottom:10px}
.footer-logo i{width:16px;height:16px;border-radius:50%;background:var(--green)}
.contact li{list-style:none;display:flex;gap:6px;align-items:center;font-size:9px;color:#d7e0da;margin-bottom:4px}
.contact i{width:8px;height:8px;border-radius:50%;background:var(--yellow);flex:none}
.footer-col h4{font-size:12px;font-weight:600;margin:8px 0 10px}
.footer-col li{list-style:none;font-size:10px;color:#d7e0da;margin-bottom:3px}
.newsletter{width:170px}
.news-form{display:flex;margin-bottom:12px}
.news-form span{flex:1;height:26px;background:#fff;border-radius:4px 0 0 4px;font-size:9px;color:#999;padding:5px 8px}
.news-form b{width:40px;height:26px;background:var(--yellow);border-radius:0 4px 4px 0}
.socials{display:flex;gap:6px}
.socials i{width:20px;height:20px;border-radius:50%;border:1px solid #cfd8d2}
.hours{font-size:10px;color:#d7e0da;margin-top:8px}
.quick-quote{width:170px;padding-top:8px}
.quick-quote h4{font-size:12px;font-weight:600;margin-bottom:8px}
.quick-quote p{font-size:9px;color:#d7e0da}
.copyright{position:absolute;left:250px;right:40px;bottom:0;height:26px;border-top:1px solid var(--green-2);font-size:9px;color:#cfd8d2;padding-top:6px}
</style>
</head>
<body>

<header class="site-header">
  <div class="brand"><span class="brand-dot"></span>Certiva</div>
  <nav class="nav"><a>Home</a><a>About Us</a><a>Services</a><a>Blog</a><a>Contact Us</a></nav>
  <div class="header-cta">
    <a class="btn">Request a Quote</a>
    <div class="phone">
      <svg width="22" height="22" viewBox="0 0 24 24"><circle cx="12" cy="12" r="12" fill="#1e3b2f"/><path d="M8.5 6.5l2 2-1.2 1.5c.8 1.6 2 2.9 3.7 3.7l1.5-1.2 2 2-1.3 1.6c-4-.6-7.7-4.3-8.3-8.3z" fill="#fff"/></svg>
      0400 555 183
    </div>
  </div>
</header>

<section class="hero">
  <div class="hero-photo ph" role="img" aria-label="Cluttered, heavily soiled room awaiting a remediation clean"></div>
  <div class="hero-shade"></div>
  <div class="hero-copy">
    <h1>Only the best service<br>for our customers</h1>
    <p>We Do The Stuff Nobody wants to do</p>
    <a class="btn">LEARN MORE</a>
  </div>
  <svg class="hero-wave" viewBox="0 0 1200 130" preserveAspectRatio="none">
    <path d="M0 70 C300 20 500 120 800 80 S1100 40 1200 60 L1200 130 L0 130Z" fill="#f5c842"/>
    <path d="M0 88 C300 40 500 135 800 98 S1100 60 1200 78 L1200 130 L0 130Z" fill="#fff"/>
  </svg>
</section>

<section class="about">
  <div class="about-media">
    <div class="ph a1" role="img" aria-label="Cleaner working in a cluttered kitchen"></div>
    <div class="ph a2" role="img" aria-label="Technician in protective suit"></div>
    <div class="ph a3" role="img" aria-label="Deep cleaning of a heavily soiled room"></div>
    <div class="years"><div class="years-icon"></div><b>30+</b><span>Years of Experience</span></div>
  </div>
  <div class="about-copy">
    <div class="eyebrow">About Us</div>
    <h2 class="title" style="font-size:28px">Delivering Quality Deep Cleaning</h2>
    <p class="lead" style="margin-top:10px;font-size:11px">Our trained crew handles the jobs others turn away, restoring homes and workplaces with careful methods, proper safety gear and a calm, respectful approach from start to finish.</p>
    <ul class="checks">
      <li><i></i>Reliable Service</li><li><i></i>Eco-Friendly</li>
      <li><i></i>Expert Cleaners</li><li><i></i>Total Excellence</li>
    </ul>
    <a class="btn">Read More
      <svg width="12" height="12" viewBox="0 0 12 12"><path d="M2 6h8M7 3l3 3-3 3" stroke="#1b1b1b" stroke-width="1.5" fill="none"/></svg></a>
  </div>
  <svg class="about-deco" viewBox="0 0 150 240"><circle cx="110" cy="120" r="90" fill="#f6f5ef"/><circle cx="110" cy="120" r="55" fill="none" stroke="#eceadf" stroke-width="10"/></svg>
</section>

<section class="services">
  <div class="ph services-photo" role="img" aria-label="Worker in hazmat suit and respirator removing waste"></div>
  <div class="services-intro">
    <div class="eyebrow" style="color:#3a3a3a">What we Provide</div>
    <h2>Our Signature Services</h2>
    <p style="font-size:11px">We step in when a space has become unsafe, using proven steps to bring it back to a healthy state.</p>
    <a class="btn">Request a Quote</a>
  </div>
  <div class="service-cards">
    <article class="card">
      <div class="card-icon"><svg width="22" height="22" viewBox="0 0 24 24"><path d="M4 14c3-6 10-8 16-6-3 1-5 4-6 7-3 0-6 0-10-1z" fill="#1e3b2f"/></svg></div>
      <h3>Pigeon Waste Clean Ups</h3>
      <p>Safe removal of droppings, nests and feathers, followed by thorough sanitising of the affected area.</p>
      <a class="btn">Read More</a>
    </article>
    <article class="card">
      <div class="card-icon"><svg width="22" height="22" viewBox="0 0 24 24"><path d="M12 2c1 4 6 6 6 12a6 6 0 0 1-12 0c0-3 2-5 3-7 0 2 1 3 2 3 0-3 0-5 1-8z" fill="#1e3b2f"/></svg></div>
      <h3>Fire Damage Clean Outs</h3>
      <p>Clearing soot, ash and debris after a fire so that repairs can begin without delay.</p>
      <a class="btn">Read More</a>
    </article>
    <article class="card">
      <div class="card-icon"><svg width="22" height="22" viewBox="0 0 24 24"><path d="M3 11l9-7 9 7v9H3z" fill="#1e3b2f"/></svg></div>
      <h3>Squalor Clean</h3>
      <p>Discreet, judgement-free clean outs that return a neglected home to a liveable condition.</p>
      <a class="btn">Read More</a>
    </article>
  </div>
  <div class="dots"><i class="on"></i><i></i><i></i></div>
</section>

<section class="why">
  <div class="why-top">
    <div>
      <div class="eyebrow">Why Choose Us</div>
      <h2 class="title">Making a Difference, One Clean at a Time</h2>
    </div>
    <p class="lead">We combine years of industry experience with modern equipment to deliver results you can see, smell and feel in every room we touch.</p>
  </div>
  <div class="stats">
    <div class="stat"><b>100%</b><span>Satisfaction Rate</span></div>
    <div class="stat"><b>180+</b><span>Successful Projects</span></div>
    <div class="stat"><b>370+</b><span>Happy Clients Served</span></div>
    <div class="stat"><b>90+</b><span>Cleaning Professionals</span></div>
  </div>
  <div class="why-video ph" role="img" aria-label="Cleaner mopping a floor beside a dark sofa">
    <div class="play"><svg width="18" height="18" viewBox="0 0 18 18"><path d="M5 3l10 6-10 6z" fill="#1b1b1b"/></svg></div>
  </div>
</section>

<section class="projects">
  <div class="eyebrow">Recent Projects</div>
  <h2 class="title">Explore the Recent Works We<br>Have Done!</h2>
  <p class="lead">A look at some of the tough jobs our team has completed, from cluttered homes to contaminated roof spaces.</p>
  <div class="project-grid">
    <div class="ph" role="img" aria-label="Rusted junk piled in an overgrown yard" style="background:linear-gradient(150deg,#4f5a34,#7d7048 60%,#3c3a2a)"></div>
    <div class="ph" role="img" aria-label="Ceiling beams coated in pigeon waste" style="background:linear-gradient(160deg,#e6e1d6,#b9b2a3 60%,#7b7466)"></div>
    <div class="ph" role="img" aria-label="Gutter filled with debris and droppings" style="background:linear-gradient(160deg,#c9cfd6,#6c6c66 60%,#2b2b28)"></div>
  </div>
  <div class="dots"><i class="on"></i><i></i><i></i></div>
</section>

<section class="cta">
  <div class="cta-bg"></div>
  <div class="ph cta-woman" role="img" aria-label="Smiling cleaner in pink gloves wiping a surface"></div>
  <div class="cta-copy">
    <div class="eyebrow">Want a Clean Home?</div>
    <h2>Experience the Best Cleaning Service Today!</h2>
    <a class="btn">Request a Quote</a>
  </div>
</section>

<section class="testimonials">
  <div class="eyebrow">Testimonials</div>
  <h2 class="title">What Our Clients are Saying<br>About Us</h2>
  <div class="stars">
    <svg width="84" height="14" viewBox="0 0 84 14" fill="#f5c842"><g id="s"><path d="M7 0l2 4.5 5 .5-3.8 3.3 1.1 5L7 10.8 2.7 13.3l1.1-5L0 5l5-.5z"/></g><use href="#s" x="17"/><use href="#s" x="34"/><use href="#s" x="51"/><use href="#s" x="68"/></svg>
  </div>
  <p class="quote">"The team arrived on time, explained every step and left the property spotless. After months of stress it was a relief to hand the job to people who truly knew what they were doing. I would recommend them to anyone facing a difficult clean."</p>
  <div class="reviewer">
    <div class="avatars"><i></i><i class="on"></i><i></i><i></i></div>
    <b>Marla Whitcombe</b><span>Happy Customer</span>
  </div>
  <div class="arrow prev"><svg width="12" height="12" viewBox="0 0 12 12"><path d="M8 2L4 6l4 4" stroke="#fff" stroke-width="2" fill="none"/></svg></div>
  <div class="arrow next"><svg width="12" height="12" viewBox="0 0 12 12"><path d="M4 2l4 4-4 4" stroke="#fff" stroke-width="2" fill="none"/></svg></div>
</section>

<section class="blog">
  <div class="eyebrow">News &amp; Articles</div>
  <h2 class="title">Discover Our Latest Blog<br>Updates</h2>
  <p class="lead">Practical advice, industry news and cleaning tips from our team to help you keep every space safe and healthy.</p>
  <div class="posts">
    <article class="post">
      <div class="ph" role="img" aria-label="Worker clearing a dusty storage room" style="background:linear-gradient(150deg,#3f3a33,#8a7a62)"></div>
      <h3>Why Professional Cleaning Saves You Time</h3>
      <a class="btn">Read More</a>
    </article>
    <article class="post">
      <div class="ph" role="img" aria-label="Furniture and waste piled in a garden" style="background:linear-gradient(150deg,#5a4c3c,#9b6e4b 50%,#4a5a3a)"></div>
      <h3>Eco-Friendly Cleaning Effective Solutions</h3>
      <a class="btn">Read More</a>
    </article>
    <article class="post">
      <div class="ph" role="img" aria-label="Cluttered workshop shelves" style="background:linear-gradient(150deg,#2f2c28,#6d6152 60%,#a89a82)"></div>
      <h3>Top 5 Tips for a Spotless Home</h3>
      <a class="btn">Read More</a>
    </article>
  </div>
  <div class="payments"><i></i><i></i><i></i><i></i><i></i><i></i><i></i></div>
</section>

<footer class="site-footer">
  <div class="footer-grid">
    <div class="footer-brand">
      <div class="footer-logo"><i></i>Certiva</div>
      <ul class="contact">
        <li><i></i>Call Us: 0400 555 183</li>
        <li><i></i>hello@certivaclean.com</li>
        <li><i></i>12 Harlow Avenue</li>
        <li><i></i>Adelaide SA 5000</li>
      </ul>
    </div>
    <div class="footer-col">
      <h4>Useful Links</h4>
      <ul><li>Home</li><li>About us</li><li>Services</li><li>Blog</li><li>Contact Us</li></ul>
    </div>
    <div class="footer-col">
      <h4>Our Services</h4>
      <ul><li>Urine Cleaning</li><li>Office Cleaning</li><li>Squalor Cleaning</li><li>Hoarder Cleaning</li><li>Window Cleaning</li></ul>
    </div>
    <div class="footer-col newsletter">
      <h4>Our Newsletter</h4>
      <div class="news-form"><span>Email address</span><b></b></div>
      <div class="socials"><i></i><i></i><i></i><i></i></div>
    </div>
    <div class="quick-quote">
      <h4>Get a Quick Quote</h4>
      <p>Need a fast price? Send us a few photos and a short description and we will reply within one business day.</p>
    </div>
  </div>
  <p class="hours">Monday to Saturday: 8:00 am to 6:00 pm</p>
  <div class="copyright">© 2025 Certiva. All Rights Reserved</div>
</footer>

</body>
</html>
```